Environmental Consultancy needs new professional Word Template for reporting

A professional looking word template that we can use for all of our reporting.

Word template needs:
- a full scale title page that we can include a different photograph on for each new project, our company logo, title, date, and client details
- Include four layered Headings, table of contents page.
- Each page (except title page) needs to be numbered, with the title of the report at the bottom of the page.
- each page needs our company logo at the top.
- Prefer it to be using similar colours to what we are currently using. Though open to new colours if you come up with something that suits what we do.

Our business is an environment/ecological consultancy and we provide a number of field and reporting based services to mining companies, government agencies, commercial developers, landholders, tourism operators etc. Some of the work we do includes:
- vegetation surveys and reporting
- fauna trapping surveys, and reporting
- water quality and aquatic ecosystem monitoring and reporting
- fish and macroinvertebrate surveys
- seagrass and coral surveys
- environmental impact statements
- environmental offsets
- rehabilitation design and monitoring
- monitoring design programs
- ecological constraints surveys.

I have attached our company logo, a copy of our current title page, and an extract of our current report style (has been greatly reduced and with client information removed). I would like sometime similar to this report style please.

Target Market(s)

Client and Government approval agencies

Industry/Entity Type

Environmental Consultant

Font styles to use
Sans Serif

Colors
faa54b
9bcb3c
00a990
83c9e6
85acd3

Requirements
Must have
• Word template needs:

```html
<!DOCTYPE html>
<html lang="en">
<head>
<meta charset="utf-8">
<title>Fernline Ecology – Report Template</title>
<link rel="stylesheet" href="https://fonts.googleapis.com/css2?family=Macondo&family=Open+Sans:ital,wght@0,400;0,600;0,700;1,400&display=swap">
<style>
  :root {
    --backdrop: #e6ddd3;
    --paper: #ffffff;
    --green: #4c7a36;
    --green-dark: #3f6a2c;
    --green-light: #d3e6c8;
    --copper: #b5673a;
    --frame: #d4b596;
    --leaf-dark: #1c2a22;
    --leaf-mid: #3b5847;
    --ink: #3a3a3a;
    --ink-soft: #6b6b6b;
  }
  * { box-sizing: border-box; margin: 0; padding: 0; }
  html, body { width: 1200px; height: 3000px; overflow: hidden; }
  body {
    background: var(--backdrop);
    font-family: "Open Sans", sans-serif;
    color: var(--ink);
    position: relative;
  }
  .page {
    position: absolute;
    width: 540px;
    height: 763px;
    background: var(--paper);
    box-shadow: 0 6px 18px rgba(80, 60, 40, 0.12);
    overflow: hidden;
  }
  .page--cover { left: 40px; top: 80px; }
  .page--contents { left: 620px; top: 80px; }
  .page--headings { left: 40px; top: 900px; }
  .page--media { left: 620px; top: 900px; }
  .page--back { left: 40px; top: 1720px; }
  .page--back-spacer { display: none; }

  .leaf-photo {
    position: absolute;
    background: radial-gradient(circle at 30% 25%, var(--leaf-mid) 0%, var(--leaf-dark) 55%),
                linear-gradient(160deg, var(--leaf-mid), var(--leaf-dark));
    background-blend-mode: normal;
  }

  /* Brand name */
  .brand {
    position: absolute;
    display: flex;
    align-items: center;
    gap: 6px;
    font-family: "Open Sans", sans-serif;
    font-weight: 400;
    color: var(--copper);
    white-space: nowrap;
  }
  .brand__dot {
    width: 8px; height: 8px; border-radius: 50%;
    background: var(--green);
  }

  /* Cover */
  .cover__photo { left: 32px; top: 40px; width: 248px; height: 683px; }
  .cover__frame {
    position: absolute; left: 62px; top: 64px; width: 420px; height: 634px;
    border: 2px solid var(--frame);
  }
  .cover__band {
    position: absolute; left: 205px; top: 393px; width: 335px; height: 216px;
    background: var(--green); color: #fff; padding: 20px 18px 0 18px;
  }
  .cover__title { font-family: "Macondo", cursive; font-size: 38px; font-weight: 400; line-height: 1.1; }
  .cover__subtitle { font-family: "Macondo", cursive; font-size: 24px; font-weight: 400; margin-top: 16px; }
  .cover__intro { font-size: 9.5px; line-height: 1.45; margin-top: 8px; }
  .cover .brand { left: 300px; top: 650px; font-size: 19px; }

  /* Running head & foot */
  .running-head {
    position: absolute; left: 52px; right: 36px; top: 36px; height: 30px;
  }
  .running-head__rule {
    position: absolute; bottom: 6px; height: 2px; background: var(--green);
  }
  .running-head .brand { top: 0; font-size: 15px; }
  .running-foot {
    position: absolute; left: 52px; right: 40px; bottom: 32px; height: 20px;
    display: flex; align-items: center;
  }
  .running-foot__rule { height: 2px; width: 160px; background: var(--copper); }
  .running-foot__title { font-size: 8px; color: var(--ink-soft); text-transform: uppercase; letter-spacing: 0.02em; }
  .page-number {
    width: 16px; height: 16px; background: var(--copper); color: #fff;
    font-size: 9px; display: flex; align-items: center; justify-content: center;
  }

  /* Contents */
  .contents { position: absolute; left: 52px; right: 52px; top: 100px; }
  .contents__title { font-size: 15px; font-weight: 700; color: var(--green-dark); margin-bottom: 10px; }
  .toc-entry {
    display: flex; align-items: baseline; font-size: 11px; line-height: 1.75; color: var(--green-dark);
  }
  .toc-entry__num { width: 32px; }
  .toc-entry__label { white-space: nowrap; }
  .toc-entry__leader { flex: 1; border-bottom: 1px dotted var(--ink-soft); margin: 0 3px; transform: translateY(-3px); }
  .toc-entry--level-1 { font-weight: 700; }
  .toc-entry--level-2 { padding-left: 32px; color: var(--ink); }
  .toc-entry--level-3 { padding-left: 32px; color: var(--ink); }
  .toc-entry--level-4 { padding-left: 32px; color: var(--ink); }
  .toc-entry--level-2 .toc-entry__num,
  .toc-entry--level-3 .toc-entry__num,
  .toc-entry--level-4 .toc-entry__num { width: 48px; }

  /* Body copy */
  .body-copy { position: absolute; left: 52px; right: 44px; top: 80px; }
  .h1 { font-size: 16px; font-weight: 700; color: var(--green-dark); margin-bottom: 12px; }
  .h2 { font-size: 13px; font-weight: 400; color: var(--green-dark); margin: 28px 0 12px; }
  .h3, .h4 { font-size: 11.5px; font-weight: 400; color: var(--green); margin: 28px 0 12px; }
  .para { font-size: 9px; line-height: 1.45; margin-bottom: 10px; }
  .special-heading {
    font-size: 9px; font-weight: 700; color: var(--copper); text-transform: uppercase;
    border-bottom: 1.5px solid var(--copper); padding-bottom: 3px; margin: 30px 0 6px;
  }
  .para--special { color: var(--copper); font-style: italic; text-align: justify; }

  /* Tables */
  .data-table { width: 100%; border-collapse: collapse; font-size: 8.5px; margin-bottom: 26px; }
  .data-table th { background: var(--green-dark); color: #fff; text-align: left; font-weight: 700; padding: 3px 6px; }
  .data-table td { padding: 3px 6px; color: var(--ink); }
  .data-table tr:nth-child(odd) td { background: var(--green-light); }
  .media__photo { position: relative; width: 100%; height: 260px; }
  .caption { font-size: 7.5px; color: var(--copper); text-align: center; margin: 4px 0 26px; }
  .bullets { list-style: none; font-size: 9px; line-height: 1.6; }
  .bullets li::before { content: "»"; color: var(--copper); margin-right: 10px; }
  .bullets li.sub { padding-left: 46px; }
  .bullets li.sub::before { content: "•"; color: var(--ink); }

  /* Back cover */
  .back__photo { left: 42px; top: 38px; width: 496px; height: 686px; }
  .back__panel {
    position: absolute; left: 232px; top: 398px; width: 306px; height: 206px;
    background: rgba(255, 255, 255, 0.9); padding: 24px 20px;
  }
  .back__panel .brand { position: static; font-size: 22px; margin-bottom: 16px; }
  .contact { list-style: none; font-size: 11px; line-height: 1.55; color: var(--ink); }
  .contact li { display: flex; gap: 8px; align-items: flex-start; }
  .contact svg { flex: none; margin-top: 3px; }
  .contact .no-icon { padding-left: 20px; }
</style>
</head>
<body>

<!-- Cover -->
<section class="page page--cover">
  <div class="leaf-photo cover__photo" role="img" aria-label="Project photograph: close-up of dark green leaves with water droplets"></div>
  <div class="cover__frame"></div>
  <div class="cover__band">
    <h1 class="cover__title">Main Title Here</h1>
    <p class="cover__subtitle">Subtitle here</p>
    <p class="cover__intro">Lorem ipsum dolor sit amet, consectetuer adipiscing elit, sed diam nonummy nibh euismod tincidunt ut laoreet dolore magna aliquam erat volutpat. Ut wisi enim ad minim veniam, quis nostrud exerci tation ullamcorper suscipit lobortis nisl ut aliquip ex ea commodo consequat. Duis</p>
  </div>
  <div class="brand"><span class="brand__dot"></span>Fernline Ecology</div>
</section>

<!-- Contents -->
<section class="page page--contents">
  <header class="running-head">
    <div class="running-head__rule" style="left:0; right:138px;"></div>
    <div class="brand" style="right:0;"><span class="brand__dot"></span>Fernline Ecology</div>
  </header>
  <nav class="contents">
    <h2 class="contents__title">Table of Contents</h2>
    <div class="toc-entry toc-entry--level-1"><span class="toc-entry__num">01.</span><span class="toc-entry__label">Heading 1</span><span class="toc-entry__leader"></span><span>3</span></div>
    <div class="toc-entry toc-entry--level-2"><span class="toc-entry__num">1.1.</span><span class="toc-entry__label">Heading 2</span><span class="toc-entry__leader"></span><span>3</span></div>
    <div class="toc-entry toc-entry--level-3"><span class="toc-entry__num">1.1.1.</span><span class="toc-entry__label">Heading 3</span><span class="toc-entry__leader"></span><span>3</span></div>
    <div class="toc-entry toc-entry--level-4"><span class="toc-entry__num">1.1.1.1.</span><span class="toc-entry__label">Heading 4</span><span class="toc-entry__leader"></span><span>3</span></div>
    <div class="toc-entry toc-entry--level-1"><span class="toc-entry__num">02.</span><span class="toc-entry__label">Tables</span><span class="toc-entry__leader"></span><span>4</span></div>
    <div class="toc-entry toc-entry--level-1"><span class="toc-entry__num">03.</span><span class="toc-entry__label">Images</span><span class="toc-entry__leader"></span><span>4</span></div>
    <div class="toc-entry toc-entry--level-1"><span class="toc-entry__num">04.</span><span class="toc-entry__label">Bullets</span><span class="toc-entry__leader"></span><span>4</span></div>
  </nav>
  <footer class="running-foot">
    <div class="running-foot__rule"></div>
    <span style="flex:1"></span>
    <span class="running-foot__title">Title of the report</span>
    <span class="page-number" style="margin-left:8px;">2</span>
  </footer>
</section>

<!-- Headings page -->
<section class="page page--headings">
  <header class="running-head">
    <div class="brand" style="left:0;"><span class="brand__dot"></span>Fernline Ecology</div>
    <div class="running-head__rule" style="left:138px; right:0;"></div>
  </header>
  <article class="body-copy">
    <h2 class="h1">01. Heading 1</h2>
    <p class="para">Lorem ipsum dolor sit amet, consectetuer adipiscing elit. Maecenas porttitor congue massa. Fusce posuere, magna sed pulvinar ultricies, purus lectus malesuada libero, sit amet commodo magna eros quis urna.</p>
    <p class="para">Nunc viverra imperdiet enim. Fusce est. Vivamus a tellus.</p>
    <h3 class="h2">1.1. Heading 2</h3>
    <p class="para">Lorem ipsum dolor sit amet, consectetuer adipiscing elit. Maecenas porttitor congue massa. Fusce posuere, magna sed pulvinar ultricies, purus lectus malesuada libero, sit amet commodo magna eros quis urna.</p>
    <p class="para">Nunc viverra imperdiet enim. Fusce est. Vivamus a tellus.</p>
    <h4 class="h3">1.1.1. Heading 3</h4>
    <p class="para">Lorem ipsum dolor sit amet, consectetuer adipiscing elit. Maecenas porttitor congue massa. Fusce posuere, magna sed pulvinar ultricies, purus lectus malesuada libero, sit amet commodo magna eros quis urna.</p>
    <p class="para">Nunc viverra imperdiet enim. Fusce est. Vivamus a tellus.</p>
    <h5 class="h4">1.1.1.1. Heading 4</h5>
    <p class="para">Lorem ipsum dolor sit amet, consectetuer adipiscing elit. Maecenas porttitor congue massa. Fusce posuere, magna sed pulvinar ultricies, purus lectus malesuada libero, sit amet commodo magna eros quis urna.</p>
    <p class="para">Nunc viverra imperdiet enim. Fusce est. Vivamus a tellus.</p>
    <h6 class="special-heading">Special heading</h6>
    <p class="para para--special">Lorem ipsum dolor sit amet, consectetuer adipiscing elit. Maecenas porttitor congue massa. Fusce posuere, magna sed pulvinar ultricies, purus lectus malesuada libero, sit amet commodo magna eros quis urna. Lorem ipsum dolor sit amet, consectetuer adipiscing elit. Maecenas porttitor congue massa. Fusce posuere, magna sed pulvinar ultricies, purus lectus malesuada libero, sit amet commodo magna eros quis urna.</p>
    <p class="para para--special">Lorem ipsum dolor sit amet, consectetuer adipiscing elit. Maecenas porttitor congue massa. Fusce posuere, magna sed pulvinar ultricies, purus lectus malesuada libero, sit amet commodo magna eros quis urna.</p>
    <p class="para para--special">Lorem ipsum dolor sit amet, consectetuer adipiscing elit. Maecenas porttitor congue massa. Fusce posuere, magna sed pulvinar ultricies, purus lectus malesuada libero, sit amet commodo magna eros quis urna.</p>
  </article>
  <footer class="running-foot">
    <span class="page-number">3</span>
    <span class="running-foot__title" style="margin-left:8px;">Title of the report</span>
    <span style="flex:1"></span>
    <div class="running-foot__rule"></div>
  </footer>
</section>

<!-- Tables, images, bullets page -->
<section class="page page--media">
  <header class="running-head">
    <div class="running-head__rule" style="left:0; right:138px;"></div>
    <div class="brand" style="right:0;"><span class="brand__dot"></span>Fernline Ecology</div>
  </header>
  <article class="body-copy" style="top:92px;">
    <h2 class="h1">02. Tables</h2>
    <table class="data-table">
      <tr><th>Title</th><th>Title</th><th>Title</th><th>Title</th></tr>
      <tr><td>00000</td><td>00000</td><td>00000</td><td>00000</td></tr>
      <tr><td>00000</td><td>00000</td><td>00000</td><td>00000</td></tr>
      <tr><td>00000</td><td>00000</td><td>00000</td><td>00000</td></tr>
      <tr><td>00000</td><td>00000</td><td>00000</td><td>00000</td></tr>
      <tr><td>00000</td><td>00000</td><td>00000</td><td>00000</td></tr>
    </table>
    <h2 class="h1">03. Images</h2>
    <div class="leaf-photo media__photo" role="img" aria-label="Report figure: dark green leaves"></div>
    <p class="caption">Figure 1: Image details here</p>
    <h2 class="h1">04. Bullets</h2>
    <ul class="bullets">
      <li>Lorem ipsum</li>
      <li class="sub">Lorem ipsum</li>
      <li>Lorem ipsum</li>
      <li>Lorem ipsum</li>
      <li>Lorem ipsum</li>
    </ul>
  </article>
  <footer class="running-foot">
    <div class="running-foot__rule"></div>
    <span style="flex:1"></span>
    <span class="running-foot__title">Title of the report</span>
    <span class="page-number" style="margin-left:8px;">4</span>
  </footer>
</section>

<!-- Back cover -->
<section class="page page--back">
  <div class="leaf-photo back__photo" role="img" aria-label="Back cover photograph: dark green leaves with water droplets"></div>
  <div class="back__panel">
    <div class="brand"><span class="brand__dot"></span>Fernline Ecology</div>
    <ul class="contact">
      <li><svg width="12" height="12" viewBox="0 0 12 12"><circle cx="6" cy="6" r="6" fill="var(--green)"/><circle cx="6" cy="6" r="3" fill="none" stroke="#fff" stroke-width="1"/><line x1="3" y1="6" x2="9" y2="6" stroke="#fff" stroke-width="0.8"/></svg>www.fernlineecology.com.au</li>
      <li><svg width="12" height="12" viewBox="0 0 12 12"><circle cx="6" cy="6" r="6" fill="var(--green)"/><rect x="3" y="4" width="6" height="4" fill="none" stroke="#fff" stroke-width="0.9"/><polyline points="3,4 6,6.3 9,4" fill="none" stroke="#fff" stroke-width="0.8"/></svg>grace@fernlineecology.com.au</li>
      <li><svg width="12" height="12" viewBox="0 0 12 12"><circle cx="6" cy="6" r="6" fill="var(--green)"/><path d="M4 3.3 L5.2 3 L5.7 4.6 L5 5.2 Q5.6 6.6 6.8 7 L7.4 6.3 L9 6.8 L8.7 8 Q5 8.5 4 3.3Z" fill="#fff"/></svg>0355501234</li>
      <li><svg width="12" height="12" viewBox="0 0 12 12"><circle cx="6" cy="6" r="6" fill="var(--green)"/><path d="M6 2.6 A2.2 2.2 0 0 1 8.2 4.8 Q8.2 6.4 6 9.2 Q3.8 6.4 3.8 4.8 A2.2 2.2 0 0 1 6 2.6Z" fill="#fff"/><circle cx="6" cy="4.8" r="0.8" fill="var(--green)"/></svg>Queensland Office</li>
      <li class="no-icon">PO Box 12, Riverton QLD 4900</li>
      <li class="no-icon">ABN 11222333444</li>
    </ul>
  </div>
</section>

</body>
</html>
```